KeyHarbor needs a modern business card

We are a modern conveyancing company and we need to appeal to the top (Multi-million dollar properties)and bottom on the property conveyancing market but our sweet spot is the middle of the market. I like professional with a hint of unconventional.

Target Market(s)

As above

Industry/Entity Type

Real Estate

Contact Information for Business Card

Back Of card:
thinking black with the logo and a tag line (I could be wrong about the black)
Tag line - Right Expertise, Exceptional Service

Front of Card:
Marissa Toll (BBus (Finance) LLB)
Licensed Conveyancer
Email: marissa@keyharbor.com.au

Key Harbor
ABN: 48 913 706
Suite 14, Level 3, 9 Calloway Road Lindhurst Park, NSW 2178
Phone: 1300 682 917

Sydney - Melbourne - Brisbane (Perhaps have this along the bottom of the card)

Requirements
Must have
• Sleek, modern and top end appeal (But approachable)
Should not have
• Not too cluttered

```html
<!DOCTYPE html>
<html lang="en">
<head>
<meta charset="utf-8">
<title>KeyHarbor Business Card</title>
<link href="https://fonts.googleapis.com/css2?family=Arimo:ital,wght@0,400;0,700;1,400&display=swap" rel="stylesheet">
<style>
  :root {
    --navy: #0d4770;
    --navy-deep: #0a3b5e;
    --white: #ffffff;
    --paper-edge: #e4e7ea;
    --stage: #eceef0;
    --ink: #1d4f7a;
  }
  * { margin: 0; padding: 0; box-sizing: border-box; }
  html, body {
    width: 1200px; height: 900px; overflow: hidden;
    background: var(--stage);
    font-family: "Arimo", Arial, sans-serif;
  }
  .card {
    position: absolute; left: 250px;
    width: 700px; height: 400px;
    background: var(--white);
    box-shadow: 0 2px 6px rgba(0,0,0,0.12);
    overflow: hidden;
  }
  .card-back { top: 40px; }
  .card-front { top: 470px; }

  /* Back */
  .brand {
    display: flex; align-items: center; gap: 14px;
    font-weight: 700; color: var(--navy);
  }
  .brand-mark { background: var(--navy); }
  .card-back .brand {
    position: absolute; top: 110px; left: 0; right: 0;
    justify-content: center; font-size: 52px;
  }
  .card-back .brand-mark { width: 38px; height: 38px; }
  .tagline-band {
    position: absolute; left: 0; right: 0; top: 248px; height: 48px;
    background: var(--navy); color: var(--white);
    display: flex; align-items: center; justify-content: center;
    font-size: 26px; letter-spacing: 0.5px; text-transform: uppercase;
  }

  /* Front */
  .front-shapes { position: absolute; inset: 0; }
  .holder {
    position: absolute; left: 46px; top: 56px; color: var(--white);
  }
  .holder-name { font-size: 30px; text-transform: uppercase; letter-spacing: 0.5px; }
  .holder-role { font-size: 18px; font-style: italic; line-height: 1.45; margin-top: 6px; }
  .holder-email {
    display: flex; align-items: center; gap: 8px;
    margin-top: 46px; font-size: 20px; font-style: italic;
  }
  .cities {
    position: absolute; left: 24px; top: 318px;
    font-size: 29px; font-style: italic; color: var(--ink);
  }
  .company {
    position: absolute; left: 490px; top: 56px; color: var(--ink);
  }
  .card-front .brand { font-size: 30px; gap: 10px; margin-bottom: 12px; }
  .card-front .brand-mark { width: 22px; height: 22px; }
  .company-details { font-size: 20px; line-height: 1.4; }
  .company-phone { display: flex; align-items: center; gap: 5px; margin-top: 2px; font-size: 22px; }
</style>
</head>
<body>

<section class="card card-back">
  <div class="brand"><span class="brand-mark"></span>KeyHarbor</div>
  <div class="tagline-band">Right Expertise, Exceptional Service</div>
</section>

<section class="card card-front">
  <svg class="front-shapes" width="700" height="400" viewBox="0 0 700 400" aria-hidden="true">
    <path d="M0 0 H412 C392 110 405 220 445 300 H0 Z" fill="var(--navy)"/>
    <path d="M440 0 H462 C436 110 446 215 478 300 C446 230 424 120 440 0 Z" fill="var(--navy)"/>
    <path d="M0 370 H480 L505 400 H0 Z" fill="var(--navy)"/>
  </svg>

  <div class="holder">
    <div class="holder-name">Marissa Toll</div>
    <div class="holder-role">(BBus (Finance) LLB)<br>Licensed Conveyancer</div>
    <div class="holder-email">
      <svg width="26" height="18" viewBox="0 0 26 18" aria-hidden="true">
        <rect x="1" y="1" width="24" height="16" fill="none" stroke="#fff" stroke-width="1.5"/>
        <path d="M1 1 L13 10 L25 1 M1 17 L10 8 M25 17 L16 8" fill="none" stroke="#fff" stroke-width="1.5"/>
      </svg>
      marissa@keyharbor.com.au
    </div>
  </div>

  <div class="cities">Sydney - Melbourne - Brisbane</div>

  <div class="company">
    <div class="brand"><span class="brand-mark"></span>KeyHarbor</div>
    <div class="company-details">
      ABN: 48 913 706<br>
      Suite 14, Level 3,<br>
      9 Calloway Road<br>
      Lindhurst Park,<br>
      NSW 2178
    </div>
    <div class="company-phone">
      <svg width="24" height="24" viewBox="0 0 24 24" aria-hidden="true">
        <circle cx="12" cy="12" r="10.5" fill="none" stroke="var(--ink)" stroke-width="1.6"/>
        <path d="M8 6.5 L10 6 L11 9 L9.8 10 C10.5 11.8 12 13.3 13.8 14 L14.8 12.8 L17.6 14 L17.2 16 C12.5 16.5 7.5 11.5 8 6.5 Z" fill="var(--ink)"/>
      </svg>
      1300 682 917
    </div>
  </div>
</section>

</body>
</html>
```